CEO of company needs clear business card that stands out from the rest

I need a clear business card (standard credit card size) for the CEO/Founder of our company...Brightfield Counseling. We would like to see designs that use our logo colors, which are khaki, chocolate brown, and gray. The card should be an edgy design, maybe where half the card is transparent with curves on the card, or a textured card where the logo is transparent, I don't care much for white cards. The final design should communicate a funky, edgy, and modern look, as well as stand out to have the "WOW" factor. The information we need on the card would be Name, Title, Toll free number, Phone Number, address, email address, and website.

*PLEASE SEND FRONT AND BACK OF CARDS

Card is two sided front and back please give us your front and back designs

The card should be an edgy design, maybe where half the card is transparent with curves on the card, or a textured card where the logo is transparent, I don't care much for white cards. The final design should communicate a funky, edgy, and modern look, as well as stand out to have the "WOW" factor.

Please follow these guidelines for the card

SPECS (card):

2.125 (h) x 3.375 (w) card size after cut

2.375 (h) x 3.625 (w) card with bleed

300 dpi

cmyk

1/8 bleed

allow 1/8 border for live area

I will also attached the pdf for the information listed above which includes a diagram of the card

 

All the cards need to have rounded edges

I just updated a card as an example of how you can use different fonts on a single business card, look how the name is written in script, so what I am saying is make this a card you will be proud to design and put it in your portfolio 

Reason: this race is really close and I am working with 2 designers to fine tune their designs and the weekend is slowing us down

• Our Logo
MUST HAVE PARTS OF CARD THAT ARE TRANSPARENT. See ideas that are attached.
Card is two sided front and back
• The final design should communicate a funky, edgy, and modern look, as well as stand out to have the "WOW" factor. The information we need on the card would be Name, Title, Toll free number, Phone Number, address, email address, and website.

```html
<!DOCTYPE html>
<html lang="en">
<head>
<meta charset="utf-8">
<title>Brightfield Counseling – Business Cards</title>
<link rel="stylesheet" href="https://fonts.googleapis.com/css2?family=Tinos:ital@0;1&display=swap">
<style>
  :root {
    --backdrop: #d9d7d3;
    --card-slate: #48484b;
    --card-slate-dark: #3c3c3f;
    --copper: #a4561d;
    --silver: #c4c4c4;
    --silver-line: #9b9b9b;
    --paper-white: #f4f4f4;
    --serif: "Tinos", "Times New Roman", serif;
  }
  * { margin: 0; padding: 0; box-sizing: border-box; }
  html, body {
    width: 1200px; height: 981px; overflow: hidden;
    background: var(--backdrop);
  }
  .stage { position: relative; width: 1200px; height: 981px; }

  .card {
    position: absolute;
    width: 700px; height: 425px;
    border-radius: 28px;
    overflow: hidden;
    background: linear-gradient(160deg, var(--card-slate) 0%, var(--card-slate-dark) 100%);
    box-shadow: 0 14px 30px rgba(0,0,0,.28);
  }
  .card-front { left: 110px; top: 48px; }
  .card-back  { left: 390px; top: 506px; }

  .card-band { position: absolute; inset: 0; width: 100%; height: 100%; }

  /* Company name (stands where the mark sits) */
  .brand-name {
    font-family: var(--serif);
    font-weight: 400;
    color: var(--silver);
    line-height: 1;
    white-space: nowrap;
    display: flex; align-items: center; gap: 12px;
  }
  .brand-dot {
    width: 12px; height: 12px; border-radius: 50%;
    background: var(--copper);
    flex: none;
  }
  .front-brand {
    position: absolute; right: 60px; top: 110px;
    font-size: 42px;
  }
  .back-brand {
    position: absolute; left: 36px; top: 52px;
    font-size: 32px;
  }

  .holder {
    position: absolute; right: 40px; top: 200px;
    text-align: center;
    font-family: var(--serif);
    color: var(--paper-white);
  }
  .holder-name { font-size: 31px; letter-spacing: .5px; }
  .holder-title { font-size: 25px; margin-top: 2px; }

  .tollfree {
    position: absolute; left: 22px; top: 346px;
    font-family: var(--serif); font-size: 14px;
    color: var(--paper-white);
  }
  .tollfree em { font-style: italic; margin-right: 8px; }

  .contact {
    position: absolute; right: 34px; top: 320px;
    list-style: none;
    font-family: var(--serif); font-size: 15.5px;
    color: var(--paper-white);
    line-height: 1.25;
  }
  .contact li { display: flex; align-items: flex-start; gap: 8px; }
  .contact .indent { padding-left: 120px; }
  .contact .addr-line2 { padding-left: 108px; }
  .contact svg { width: 14px; height: 14px; margin-top: 2px; flex: none; fill: var(--paper-white); }
</style>
</head>
<body>
<main class="stage">

  <section class="card card-front" aria-label="Card front">
    <svg class="card-band" viewBox="0 0 700 425" preserveAspectRatio="none" aria-hidden="true">
      <path d="M0 372 L250 360 C330 354 340 300 420 286 L700 238 L700 425 L0 425 Z" fill="var(--copper)"/>
      <path d="M0 372 L250 360 C330 354 340 300 420 286 L700 238" fill="none" stroke="var(--silver-line)" stroke-width="5"/>
    </svg>
    <div class="brand-name front-brand"><span class="brand-dot"></span>Brightfield Counseling</div>
  </section>

  <section class="card card-back" aria-label="Card back">
    <svg class="card-band" viewBox="0 0 700 425" preserveAspectRatio="none" aria-hidden="true">
      <path d="M0 282 L180 288 C240 290 260 318 310 318 C360 318 380 282 440 282 L700 300 L700 425 L0 425 Z" fill="var(--copper)"/>
      <path d="M0 282 L180 288 C240 290 260 318 310 318 C360 318 380 282 440 282 L700 300" fill="none" stroke="var(--silver-line)" stroke-width="5"/>
    </svg>
    <div class="brand-name back-brand"><span class="brand-dot"></span>Brightfield Counseling</div>

    <div class="holder">
      <div class="holder-name">Darren Whitfield</div>
      <div class="holder-title">Founder / CEO</div>
    </div>

    <p class="tollfree"><em>Toll Free #:</em>1.855.555.0164</p>

    <ul class="contact">
      <li class="indent">
        <svg viewBox="0 0 24 24" aria-label="Phone"><path d="M6.6 10.8a15 15 0 0 0 6.6 6.6l2.2-2.2c.3-.3.7-.4 1-.2 1.1.4 2.3.6 3.6.6.6 0 1 .4 1 1V20c0 .6-.4 1-1 1A17 17 0 0 1 3 4c0-.6.4-1 1-1h3.5c.6 0 1 .4 1 1 0 1.3.2 2.5.6 3.6.1.3 0 .7-.2 1z"/></svg>
        404.555.0142
      </li>
      <li class="indent">
        <svg viewBox="0 0 24 24" aria-label="Fax"><path d="M6 3h12v5H6zM4 9h16a2 2 0 0 1 2 2v6h-4v4H6v-4H2v-6a2 2 0 0 1 2-2zm4 7v3h8v-3z"/></svg>
        678.555.0187
      </li>
      <li>
        <svg viewBox="0 0 24 24" aria-label="Email"><path d="M2 5h20v14H2zm2 2v.5l8 5 8-5V7zm0 3v7h16v-7l-8 5z"/></svg>
        dwhitfield@brightfieldcounseling.com
      </li>
      <li>
        <svg viewBox="0 0 24 24" aria-label="Address"><path d="M12 2a7 7 0 0 1 7 7c0 5-7 13-7 13S5 14 5 9a7 7 0 0 1 7-7zm0 4.5a2.5 2.5 0 1 0 0 5 2.5 2.5 0 0 0 0-5z"/></svg>
        4410 Alder Ridge Dr. N.W. Suite 210
      </li>
      <li class="addr-line2">Marietta, GA 30067</li>
    </ul>
  </section>

</main>
</body>
</html>
```